Professional
Miriam T. Hollisby, Esq.
Attorney at Law
Hollisby & Dunmore, LLC
4127 Fernhaven Court
Atlanta, Georgia 30305
mhollisby@hd-counsel.net
www.hd-counsel.net
I may want to include a photo. I have uploaded a photo. I'd like to see if it looks appropriate, if not, we'll go without a photo. Please use the logo that is uploaded
Please use the logo that is uploaded in some way. Possibly the corresponding black background with whitel letters for the back.
Photo to possibly be included on busines cards

```html
<!DOCTYPE html>
<html lang="en">
<head>
<meta charset="utf-8">
<title>Hollisby &amp; Dunmore, LLC — Business Cards</title>
<link rel="stylesheet" href="https://fonts.googleapis.com/css2?family=Marcellus+SC&display=swap">
<style>
  :root {
    --backdrop: #e7e4e0;
    --paper: #ffffff;
    --ink: #2b2b2b;
    --ink-soft: #555555;
    --night: #050505;
    --crimson: #c4161c;
    --crimson-deep: #6e0a0c;
    --crimson-mid: #a3161a;
    --on-red: #f4dede;
    --rule: #c9c9c9;
  }
  * { box-sizing: border-box; margin: 0; padding: 0; }
  html, body { width: 1200px; height: 754px; overflow: hidden; }
  body {
    background: var(--backdrop);
    font-family: "Marcellus SC", "Times New Roman", serif;
    color: var(--ink);
    position: relative;
  }
  .card {
    position: absolute;
    overflow: hidden;
    box-shadow: 0 3px 10px rgba(0,0,0,.18);
  }
  .card--front { left: 288px; top: 43px; width: 547px; height: 336px; background: var(--paper); }
  .card--back-dark { left: 53px; top: 384px; width: 523px; height: 312px; background: var(--night); }
  .card--back-light { left: 617px; top: 384px; width: 523px; height: 312px; background: var(--paper); }

  .lockup {
    position: absolute;
    display: flex;
    align-items: center;
    gap: 14px;
    white-space: nowrap;
  }
  .lockup__dot {
    width: 34px; height: 34px;
    border-radius: 50%;
    background: var(--crimson);
    flex: none;
  }
  .lockup__name { font-size: 25px; letter-spacing: .5px; color: var(--ink); }
  .card--front .lockup { left: 50%; top: 92px; transform: translateX(-50%); }
  .card--back-dark .lockup { left: 50%; top: 50%; transform: translate(-50%, -50%); }
  .card--back-dark .lockup__name { color: #ffffff; font-size: 27px; }
  .card--back-light .lockup { left: 50%; top: 50%; transform: translate(-50%, -50%); }
  .card--back-light .lockup__name { font-size: 27px; }

  .contact-band {
    position: absolute;
    left: 0; right: 0; top: 182px; bottom: 0;
    background: radial-gradient(ellipse at 50% 45%, var(--crimson-mid) 0%, var(--crimson-deep) 85%);
    border-top: 3px solid var(--paper);
    box-shadow: inset 0 2px 0 var(--crimson-deep);
    color: var(--on-red);
  }
  .contact-band__details {
    position: absolute;
    right: 270px; top: 24px;
    text-align: right;
    font-size: 10.5px;
    line-height: 14px;
  }
  .contact-band__details .gap { height: 12px; }
  .contact-band__divider {
    position: absolute;
    left: 287px; top: 22px; width: 1px; height: 110px;
    background: rgba(255,255,255,.5);
  }
  .contact-band__person {
    position: absolute;
    left: 302px; top: 50px;
    white-space: nowrap;
  }
  .person__name { font-size: 17px; color: #ffffff; }
  .person__title { font-size: 10.5px; margin-top: 2px; }
</style>
</head>
<body>
  <section class="card card--front">
    <div class="lockup">
      <span class="lockup__dot"></span>
      <span class="lockup__name">Hollisby &amp; Dunmore, LLC</span>
    </div>
    <div class="contact-band">
      <div class="contact-band__details">
        <div>Hollisby &amp; Dunmore, LLC</div>
        <div>4127 Fernhaven Court</div>
        <div>Atlanta, Georgia 30305</div>
        <div class="gap"></div>
        <div>P: 404-555-0178</div>
        <div>F: 404-555-0179</div>
        <div>E: mhollisby@hd-counsel.net</div>
        <div class="gap"></div>
        <div>W: www.hd-counsel.net</div>
      </div>
      <div class="contact-band__divider"></div>
      <div class="contact-band__person">
        <div class="person__name">Miriam T. Hollisby, Esq.</div>
        <div class="person__title">Attorney at Law</div>
      </div>
    </div>
  </section>

  <section class="card card--back-dark">
    <div class="lockup">
      <span class="lockup__dot"></span>
      <span class="lockup__name">Hollisby &amp; Dunmore, LLC</span>
    </div>
  </section>

  <section class="card card--back-light">
    <div class="lockup">
      <span class="lockup__dot"></span>
      <span class="lockup__name">Hollisby &amp; Dunmore, LLC</span>
    </div>
  </section>
</body>
</html>
```